Tallowmoor Letterheads Design

Hello, we have just upgraded this project for a guaranteed payment.

We are currently going through a re-branding exercise internally. Our logo is attached as a PDF file.

We are happy with our logo but would like to investigate how we can best apply the logo to our letterheads and compliment slips.

We are a quality printing company in England. Despite our name we are very professional and offer a personal service.

Our new website is under construction and here is a link to show you how it looks: http://brackenpress.v4ntor.co.uk

The style must be professional and steer away from "tacky" otherwise it makes our company look very low budget and just a bit silly.

We would like to see elements of creativity though, so please, nothing too boring.

I have attached our new logo, there is an option for use on white or black.

Cheers
Tallowmoor Team

Reason: We have increased the deadline due to an internal delay to things, we now have more time before we need anything to be printed.

Industry/Entity Type

Construction

Requirements
Must have
• IMPORTANT! Please do not tweak or change our logo in any way. A few designs show vast changes in the logo, this is not what we require. Please do not change the logo in any way. Thanks
Nice to have
• Classy but approachable. Elements of "quirky" would be nice to see.
Should not have
• A Tacky feel

```html
<!DOCTYPE html>
<html lang="en">
<head>
<meta charset="utf-8">
<title>Tallowmoor – With Compliments Slip</title>
<link rel="stylesheet" href="https://fonts.googleapis.com/css2?family=Montserrat:wght@400;700&family=Roboto:wght@300&display=swap">
<style>
  :root {
    --panel-dark: #1b2023;
    --paper: #ffffff;
    --brand-pink: #e8187f;
    --ink: #1b2023;
    --watermark: #f2f2f2;
    --heading-ink: #222222;
  }
  html, body {
    margin: 0;
    padding: 0;
    overflow: hidden;
    background: var(--paper);
  }
  .slip {
    position: relative;
    width: 1200px;
    height: 567px;
    background: var(--paper);
    overflow: hidden;
  }
  .side-panel {
    position: absolute;
    left: 0;
    top: 0;
    width: 286px;
    height: 567px;
    background: var(--panel-dark);
  }
  .brand {
    position: absolute;
    left: 0;
    top: 30px;
    width: 286px;
    text-align: center;
    color: var(--paper);
    font-family: "Montserrat", sans-serif;
  }
  .brand-dot {
    display: block;
    width: 56px;
    height: 56px;
    margin: 0 auto 18px;
    border-radius: 50%;
    background: var(--brand-pink);
  }
  .brand-name {
    display: block;
    font-weight: 700;
    font-size: 34px;
    letter-spacing: -0.5px;
    line-height: 1;
  }
  .brand-tagline {
    display: block;
    margin-top: 6px;
    font-weight: 400;
    font-size: 14px;
  }
  .contact-cloud {
    position: absolute;
    left: 26px;
    top: 368px;
    width: 244px;
    height: 172px;
  }
  .contact-details {
    position: absolute;
    left: 34px;
    top: 412px;
    margin: 0;
    padding: 0;
    list-style: none;
    font-family: "Montserrat", sans-serif;
    font-size: 13px;
    line-height: 16px;
    color: var(--ink);
  }
  .contact-details li::before {
    content: "•";
    margin-right: 2px;
  }
  .contact-details .web {
    font-weight: 700;
    margin-top: 2px;
  }
  .compliments-heading {
    position: absolute;
    right: 34px;
    top: 22px;
    margin: 0;
    font-family: "Roboto", sans-serif;
    font-weight: 300;
    font-size: 29px;
    letter-spacing: 0.5px;
    color: var(--heading-ink);
  }
  .watermark {
    position: absolute;
    left: 560px;
    top: 120px;
    width: 560px;
    height: 430px;
    border-radius: 50%;
    background: radial-gradient(ellipse at center, var(--watermark) 0%, var(--watermark) 55%, rgba(242,242,242,0) 72%);
  }
</style>
</head>
<body>
  <main class="slip">
    <div class="watermark" role="img" aria-label="Faint large brand watermark"></div>

    <h1 class="compliments-heading">WITH COMPLIMENTS</h1>

    <aside class="side-panel">
      <div class="brand">
        <span class="brand-dot"></span>
        <span class="brand-name">Tallowmoor</span>
        <span class="brand-tagline">Quality Printing</span>
      </div>

      <svg class="contact-cloud" viewBox="0 0 244 172" aria-hidden="true">
        <path fill="#ffffff" d="M0 172 V28 Q0 14 14 14 Q22 2 36 8 Q48 0 62 8 Q76 14 90 10 Q112 18 134 12 Q160 6 180 10 Q200 -2 220 6 Q244 8 244 30 V172 Z"/>
      </svg>

      <ul class="contact-details">
        <li>17 Mill Lane,<br>&nbsp;&nbsp;Ashby-Under-The-Fell,<br>&nbsp;&nbsp;Ashby, Dorset,<br>&nbsp;&nbsp;DT4 8QE</li>
        <li>Tel: 0207 946 0832</li>
        <li class="web">www.brackenpress.v4ntor.co.uk</li>
      </ul>
    </aside>
  </main>
</body>
</html>
```